依頼詳細
お客様に見積もり・図面などを提出する時に使用する封筒です。使用用途は幅広く、その他にも取引業者さまへのお手紙を出す時にも使います。

弊社は新築住宅・リフォーム工事を施工しているため、どちらのお客様にも使用できるよう、シンプルでかっこいいデザインをもとめています。
裏ありでも、なしでも構いません。

ロゴ添付しましたが、使用してもしなくても、構いません。

参考に弊社のホームページです

URL: https://www.bluecrestyuzawa.jp/
記載項目
北森燃料株式会社 住宅事業部 BLUE CREST
■白峰台ショールーム
〒998-0412
東雲県白峰郡桜沢町白峰台岡平34-8
■住宅事業部 本店事務所
〒998-0413
東雲県白峰郡桜沢町鶴間台柳原下平地52-6

※ここより下は2店の共通事項になります↓
TEL: 0199-94-7201 FAX: 0199-94-7216
Email: bluecrest.info@kitamori-nenryo.com
希望イメージ
シンプル 複雑
単色 カラフル
暗い 明るい
日常 高級
遊び心 厳粛
未来的 伝統的
女性的 男性的
希望する色
グレー系
納品ファイル
• イラストレーター形式 (.ai)
補足説明
ツバサプリント様にすぐ入稿できる形での納品をお願い致します。
※継続依頼あります。宜しくお願い致します。
■ 選んだ理由

『シンプルでかっこいい』という依頼通りのデザインでとても気に入りました。沢山デザインして頂き、ありがとうございます。丁寧で誠実な対応に感謝です。是非又何かありましたら、宜しくお願い致します。

■ 提案者全員のお礼・コメント

今回、報酬が安価に関わらず、沢山のランサー様が素敵なデザインを作成して頂きました!本当にありがとうございました。

```html
<!DOCTYPE html>
<html lang="ja">
<head>
<meta charset="utf-8">
<title>北森燃料株式会社 住宅事業部 封筒</title>
<link rel="stylesheet" href="https://fonts.googleapis.com/css2?family=Noto+Sans+JP:wght@400;500&family=Montserrat:wght@500;600&display=swap">
<style>
  :root {
    --page: #ffffff;
    --paper: #cdcdcd;
    --paper-edge: #b5b5b5;
    --ink: #4f4f4f;
    --ink-soft: #666666;
  }
  html, body {
    margin: 0;
    padding: 0;
    width: 849px;
    height: 1200px;
    overflow: hidden;
    background: var(--page);
  }
  .canvas {
    position: relative;
    width: 849px;
    height: 1200px;
    font-family: "Noto Sans JP", sans-serif;
    color: var(--ink);
  }
  .envelope-shape {
    position: absolute;
    left: 0;
    top: 0;
  }
  .brand-mark {
    position: absolute;
    left: 0;
    width: 849px;
    top: 895px;
    text-align: center;
  }
  .brand-mark__square {
    display: block;
    width: 40px;
    height: 40px;
    margin: 0 auto 10px;
    background: var(--ink);
  }
  .brand-mark__name {
    font-family: "Montserrat", sans-serif;
    font-weight: 600;
    font-size: 13px;
    letter-spacing: 0.3em;
    color: var(--ink);
  }
  .sender-name {
    position: absolute;
    left: 100px;
    top: 1018px;
    font-size: 15px;
    font-weight: 500;
    letter-spacing: 0.12em;
    white-space: nowrap;
  }
  .sender-name .en {
    font-family: "Montserrat", sans-serif;
    letter-spacing: 0.14em;
  }
  .sender-rule {
    position: absolute;
    left: 100px;
    top: 1048px;
    width: 650px;
    height: 1px;
    background: var(--ink-soft);
  }
  .locations {
    position: absolute;
    left: 100px;
    top: 1062px;
    font-size: 10.5px;
    line-height: 1.55;
    color: var(--ink-soft);
    white-space: nowrap;
  }
  .location + .location { margin-top: 10px; }
  .location p { margin: 0; }
  .contact {
    position: absolute;
    left: 496px;
    top: 1064px;
    font-family: "Montserrat", sans-serif;
    font-size: 10.5px;
    line-height: 1.5;
    color: var(--ink-soft);
    letter-spacing: 0.04em;
    white-space: nowrap;
  }
  .contact p { margin: 0; }
</style>
</head>
<body>
<div class="canvas">
  <svg class="envelope-shape" width="849" height="1200" viewBox="0 0 849 1200" aria-hidden="true">
    <path d="M85 62 L92 28 L757 28 L764 62 Z" fill="var(--paper)" stroke="var(--paper-edge)" stroke-width="1"/>
    <rect x="85" y="62" width="679" height="1113" fill="var(--paper)" stroke="var(--paper-edge)" stroke-width="1"/>
    <line x1="85" y1="62" x2="764" y2="62" stroke="var(--paper-edge)" stroke-width="1"/>
  </svg>

  <div class="brand-mark">
    <span class="brand-mark__square"></span>
    <span class="brand-mark__name">BLUE CREST</span>
  </div>

  <div class="sender-name">北森燃料株式会社　住宅事業部　<span class="en">BLUE CREST</span></div>
  <div class="sender-rule"></div>

  <div class="locations">
    <div class="location">
      <p>白峰台ショールーム</p>
      <p>〒998-0412　東雲県白峰郡桜沢町白峰台岡平34-8</p>
    </div>
    <div class="location">
      <p>住宅事業部 本店事務所</p>
      <p>〒998-0413　東雲県白峰郡桜沢町鶴間台柳原下平地52-6</p>
    </div>
  </div>

  <div class="contact">
    <p>TEL: 0199-94-7201</p>
    <p>FAX: 0199-94-7216</p>
    <p>Email: bluecrest.info@kitamori-nenryo.com</p>
    <p>URL: https://www.bluecrestyuzawa.jp/</p>
  </div>
</div>
</body>
</html>
```